Business cards and Stationary | Corvel Music Events

Hello! We need business cards and stationery for a new small business in the music industry. "Corvel is a high-end music agency which provides an unparalleled level of talent and personalized service to the realm entertainment, corporate events, and luxury weddings. Here is where the classical meets the contemporary and we can bring your vision to life.Keeping a steady finger on the pulse of current trends and consistently raising the bar for industry standards, Corvel continues to rise to the forefront of the music industry, providing the utmost professional, high-end, elegant, and engaging entertainment in Australia and World-Wide."

Target Market(s)

Class A. high profile corporate business.

Industry/Entity Type

Entertainment

Contact Information for Business Card

Corvel Music Events

Tessa Holloway
Director | Violinist

Level 7, 41 Marlow Street
Sydney, 2000

Website: www.corvelmusicevents.com
Phone number: 0481 352 604
Email: tessa@corvelmusicevents.com

Font styles to use
Serif
Sans Serif
Script

Colors
feeeee
0355a3
f59296
ffffff

Requirements
Nice to have
• Clean and sophisticated would be perfect.
• If there is a way to include the Instagram without being tacky, that would be awesome
• @corvelmusicevents
• Our website and logo have the following fonts:
• The primary logo is inspired and based on a font called BillionScript but the B is completely hand drawn and the rest is customised a bit to work together cohesively
• Monserrat Light - Is the Music part of the logo and as headers in the site
• Open Sans 300 and 400 (Light or Regular) is used mostly as the body text in the site
• If you want to access the website:
• www.corvelmusicevents.com
• username: client
• password: preview

```html
<!DOCTYPE html>
<html lang="en">
<head>
<meta charset="utf-8">
<title>Corvel Music Events – Business Card</title>
<link rel="stylesheet" href="https://fonts.googleapis.com/css2?family=Open+Sans:wght@300;400;700&display=swap">
<style>
  :root{
    --backdrop:#3b3d40;
    --rose:#c99a9a;
    --rose-deep:#b98687;
    --charcoal:#4a4d52;
    --paper:#ffffff;
    --ink:#3c3c3e;
    --icon:#c48f90;
  }
  *{margin:0;padding:0;box-sizing:border-box}
  html,body{width:1200px;height:1000px;overflow:hidden}
  body{background:var(--backdrop);font-family:"Open Sans",Arial,sans-serif;position:relative}

  .card{position:absolute;width:700px;height:400px;overflow:hidden;
        box-shadow:0 14px 30px rgba(0,0,0,.35)}

  /* back of card */
  .card-back{left:420px;top:90px;background:var(--rose)}
  .card-back .brand{position:absolute;left:0;right:0;top:130px;text-align:center;
        font-weight:300;font-size:76px;color:var(--paper);letter-spacing:2px}
  .card-back .brand-dot{position:absolute;left:50%;top:95px;width:36px;height:36px;
        margin-left:-18px;border:2px solid var(--paper);border-radius:50%}
  .card-back .site{position:absolute;left:0;right:0;top:268px;text-align:center;
        font-weight:400;font-size:17px;letter-spacing:2px;color:var(--paper)}

  /* front of card */
  .card-front{left:90px;top:420px;background:var(--paper)}
  .card-front .wave{position:absolute;inset:0}
  .holder{position:absolute;right:38px;top:118px;text-align:right;color:var(--paper)}
  .holder-name{font-weight:700;font-size:22px;letter-spacing:1px}
  .holder-role{font-weight:400;font-size:17px;letter-spacing:.5px;margin-top:-2px}

  .brand-front{position:absolute;left:58px;top:70px;color:var(--rose-deep);font-weight:300}
  .brand-front .word{display:block;font-size:58px;line-height:1}
  .brand-front .sub{display:block;font-size:16px;letter-spacing:6px;margin-left:96px;margin-top:2px}

  .contact{position:absolute;left:40px;top:248px;color:var(--ink);font-size:17px;font-weight:400}
  .contact .address{margin-bottom:8px}
  .contact .cols{display:flex;gap:44px}
  .contact ul{list-style:none}
  .contact li{display:flex;align-items:center;gap:8px;height:26px}
  .contact svg{width:16px;height:16px;flex:none}
</style>
</head>
<body>

  <section class="card card-back" aria-label="Business card back">
    <div class="brand-dot"></div>
    <div class="brand">Corvel</div>
    <div class="site">www.corvelmusicevents.com</div>
  </section>

  <section class="card card-front" aria-label="Business card front">
    <svg class="wave" viewBox="0 0 700 400" preserveAspectRatio="none">
      <path fill="var(--rose)" d="M0,0 H700 V212 C590,222 500,195 400,120 C310,55 170,30 0,72 Z"/>
      <path fill="none" stroke="var(--charcoal)" stroke-width="9"
            d="M190,54 C270,62 330,90 405,142 C500,208 590,226 700,218"/>
      <path fill="none" stroke="var(--rose)" stroke-width="2"
            d="M0,84 C120,55 200,48 240,50"/>
    </svg>

    <div class="brand-front">
      <span class="word">Corvel</span>
      <span class="sub">MUSIC</span>
    </div>

    <div class="holder">
      <div class="holder-name">TESSA HOLLOWAY</div>
      <div class="holder-role">PRESIDENT</div>
    </div>

    <div class="contact">
      <p class="address">Level 7, 41 Marlow Street Sydney, 2000</p>
      <div class="cols">
        <ul>
          <li><svg viewBox="0 0 16 16"><path fill="var(--icon)" d="M2 6c0-2 2-3 6-3s6 1 6 3l-1 1-2-1V5H5v1L3 7zM4 8h8l1 5H3z"/></svg>0481 352 604</li>
          <li><svg viewBox="0 0 16 16"><rect x="4" y="1" width="8" height="14" rx="1.5" fill="none" stroke="var(--icon)" stroke-width="1.6"/><rect x="7" y="12" width="2" height="1.4" fill="var(--icon)"/></svg>0481 352 604</li>
        </ul>
        <ul>
          <li><svg viewBox="0 0 16 16"><rect x="1" y="3" width="14" height="10" fill="var(--icon)"/><path d="M1 3l7 6 7-6" fill="none" stroke="#fff" stroke-width="1.3"/></svg>instagram@corvelmusicevents</li>
          <li><svg viewBox="0 0 16 16"><circle cx="8" cy="8" r="7" fill="var(--icon)"/><path d="M1 8h14M8 1c-3 4-3 10 0 14M8 1c3 4 3 10 0 14" fill="none" stroke="#fff" stroke-width="1"/></svg>www.corvelmusicevents.com</li>
        </ul>
      </div>
    </div>
  </section>

</body>
</html>
```